LumoPledge Crowdfunding Website 1st Page

I am looking to have a first page created for a new crowd funding website that knocks down the biggest hurdle that creative types and start ups face, legal costs. For creative projects and innovative products, we are providing intellectual property and certain other legal services wrapped into the project costs.

I am using a white label crowdfunding platform that that has a standard look and feel of most crowdfunding sites e.g. tiles with campaigns, listing of campaigns categories, create new campaign options, and donate to campaigns etc. The white label program is branded with the LumoPledge logo and colors. At present there is a front page that is just a place holder for someone at ArtHively's great design! What I need is an eye-catching first page that visually and through content optimizes the LumoPledge brand. (There should be space for content for those looking to raise money and those looking to donate to campaigns.)

www.fundvexora.com is, of course, the reigning King of crowdfunding. They have been so successful that they no longer have to entice people to launch campaigns there. (So they don't speak as much to those looking to raise money.) Unlike Fundvexora, of the challenges is that I have two customers I need to engage. The first is the potential crowdfund campaign owner who is looking to raise money. The second customer is the donor.

I am looking for a smart page from a marketing standpoint that also grabs you. One should feel the energy of "the crowd" when they look at the page.

Some information regarding the logo: The font is Kabel BK BT. The primary blue is R33, G121, B 159. Hex21799F and the primary greenis R179, G210, B54 Hex B3D236. The third file is a slight variation on the LP logo that you are free to use as well. (Unfortunately, I don't have all the color information for that one readily available.) If you need more files, please just let me know.

Industry/Entity Type

Marketing

Font styles to use
Other font styles liked:
• Kabel Bk BT or complimentary

Requirements
Must have
• Please use the slogan "Where the crowd meets great ideas".

```html
<!DOCTYPE html>
<html lang="en">
<head>
<meta charset="utf-8">
<title>LumoPledge – Where the crowd meets great ideas</title>
<link href="https://fonts.googleapis.com/css2?family=Didact+Gothic&family=Open+Sans:wght@400;600;700&display=swap" rel="stylesheet">
<style>
:root{
  --blue:#21799f;
  --green:#8cc63f;
  --green-dark:#76ad2c;
  --red:#d9413a;
  --ink:#333;
  --muted:#666;
  --line:#dcdcdc;
  --hero-a:#f6fafc;
  --hero-b:#d7e7ef;
  --grey-band:#efefef;
  --footer:#f4f4f4;
  --bar:#333;
  --white:#fff;
}
*{box-sizing:border-box;margin:0;padding:0}
html,body{width:743px;height:1200px;overflow:hidden}
body{position:relative;background:var(--white);font-family:"Open Sans",Arial,sans-serif;color:var(--ink);font-size:8px}
.abs{position:absolute}
.display{font-family:"Didact Gothic","Century Gothic",sans-serif}

/* header */
.site-header{left:0;top:0;width:743px;height:60px;background:var(--white)}
.brand{left:78px;top:8px;display:flex;align-items:center;gap:6px}
.brand-dot{width:30px;height:30px;border-radius:50%;background:var(--green)}
.brand-name{font-family:"Didact Gothic",sans-serif;font-size:17px;color:var(--blue);padding-top:18px}
.search{left:469px;top:5px;width:126px;height:14px;border:1px solid var(--line);border-radius:2px;font-size:6px;color:#999;padding:2px 5px}
.search svg{position:absolute;right:4px;top:3px}
.account{left:604px;top:6px;font-size:7.5px;color:#888}
.nav{left:305px;top:31px;display:flex;gap:0;font-size:7.5px;font-weight:700;color:#444}
.nav a{text-decoration:none;color:inherit;padding:0 10px;position:relative}
.nav .active:after{content:"";position:absolute;left:7px;right:7px;top:14px;height:2px;background:var(--green)}

/* hero */
.hero{left:0;top:60px;width:743px;height:236px;background:radial-gradient(ellipse at 35% 30%,var(--hero-a),var(--hero-b))}
.hero-title{left:0;width:743px;top:46px;text-align:center;font-size:26px;color:var(--blue)}
.hero-list{left:140px;top:100px;list-style:none}
.hero-list li{display:flex;align-items:center;gap:14px;height:35px;font-size:12.5px;color:var(--blue)}
.tick{width:16px;height:16px;border-radius:50%;background:#e8f1dc;display:flex;align-items:center;justify-content:center}
.coins{left:476px;top:93px;width:170px;height:110px;border-radius:40px 40px 10px 10px;background:radial-gradient(ellipse at 50% 40%,#f7d24d,#d7a21c 70%,rgba(215,162,28,0))}
.arrow{top:152px}

/* discover */
.discover-title{left:79px;top:316px;font-size:19.5px;line-height:24px;color:var(--blue)}
.discover-text{left:79px;top:372px;width:350px;font-size:7.5px;line-height:12px;color:var(--muted)}
.start-btn{left:472px;top:340px;width:147px;height:36px;border-radius:18px;background:var(--green);color:var(--white);font-family:"Didact Gothic",sans-serif;font-size:14px;display:flex;align-items:center;padding-left:18px;gap:18px}

/* projects band */
.projects{left:0;top:422px;width:743px;height:428px;background:var(--grey-band)}
.tabs{left:204px;top:442px;width:342px;height:25px;border-radius:13px;background:var(--white);display:flex;align-items:center;justify-content:space-around;font-size:7px;color:#444;box-shadow:0 0 2px rgba(0,0,0,.1)}
.tabs span{display:flex;align-items:center;gap:5px}
.categories{left:79px;top:496px;width:112px;list-style:none}
.categories li{height:22.9px;line-height:22px;font-size:9.5px;color:#444;border-bottom:1px solid var(--line)}
.more-link{left:79px;top:825px;font-size:7px;font-weight:700;color:var(--green-dark)}
.view-all{left:633px;top:823px;font-size:7.5px;font-weight:700;color:#222}

.card{width:141px;height:159px;background:var(--white)}
.card-media{position:relative;height:72px}
.price{position:absolute;left:0;right:0;bottom:0;height:18px;background:rgba(40,40,40,.85);color:var(--white);font-size:12.5px;padding:1px 8px}
.card-body{padding:4px 8px}
.card-name{font-size:7.5px;font-weight:700;color:var(--green-dark)}
.card-text{font-size:7px;line-height:9.5px;color:var(--muted);margin-top:2px}
.progress{margin-top:7px;height:6px;border-radius:3px;background:#e5e5e5;overflow:hidden}
.progress i{display:block;height:100%;background:var(--green)}
.progress.late i{background:var(--red)}
.stats{display:flex;justify-content:space-between;margin-top:8px;font-size:6.8px;color:#555;line-height:9px}
.stats b{display:block;font-weight:400;color:var(--green-dark)}

/* stories */
.stories-title{left:0;width:743px;top:862px;text-align:center;font-size:19px;color:#333}
.stories-text{left:215px;width:313px;top:896px;text-align:center;font-size:7.5px;line-height:12px;color:var(--muted)}
.avatar{width:58px;height:58px;border-radius:50%;top:935px}

/* footer */
.site-footer{left:0;top:1027px;width:743px;height:131px;background:var(--footer)}
.foot-h{top:1042px;font-size:12.5px;color:#333}
.foot-p{font-size:7.5px;line-height:11.5px;color:#444}
.foot-links{list-style:none;font-size:7px;color:#444}
.foot-links li{height:15px}
.newsletter{left:460px;top:1119px;width:181px;height:26px;border-radius:13px;background:var(--white);border:1px solid var(--line);font-size:7px;font-weight:600;color:#888;padding:8px 12px}
.subscribe{position:absolute;right:-1px;top:-1px;width:60px;height:26px;border-radius:13px;background:var(--green);color:var(--white);font-size:6.5px;font-weight:700;text-align:center;line-height:26px}
.bottom-bar{left:0;top:1158px;width:743px;height:42px;background:var(--bar);color:#999;font-size:7px;padding:16px 90px}
</style>
</head>
<body>

<header class="site-header abs">
  <div class="brand abs"><span class="brand-dot"></span><span class="brand-name">LumoPledge</span></div>
  <div class="search abs">Enter keyword here
    <svg width="8" height="8" viewBox="0 0 8 8"><circle cx="3.3" cy="3.3" r="2.3" fill="none" stroke="#777" stroke-width="1"/><path d="M5 5l2.3 2.3" stroke="#777" stroke-width="1"/></svg>
  </div>
  <div class="account abs">Sign up &nbsp;|&nbsp; Login</div>
  <nav class="nav abs">
    <a class="active">HOME</a><a>WHO WE ARE</a><a>SUCCESS FULL STORIES</a><a>QUESTIONS</a><a>HELP</a><a>CONTACT</a>
  </nav>
</header>

<section class="hero abs">
  <h1 class="hero-title abs display">Where the crowd meets great ideas !</h1>
  <ul class="hero-list abs display">
    <li><span class="tick"><svg width="10" height="10" viewBox="0 0 10 10"><path d="M1.5 5.2l2.4 2.4 4.6-5" fill="none" stroke="#8cc63f" stroke-width="1.8"/></svg></span>when an unknown printer took a galley of type</li>
    <li><span class="tick"><svg width="10" height="10" viewBox="0 0 10 10"><path d="M1.5 5.2l2.4 2.4 4.6-5" fill="none" stroke="#8cc63f" stroke-width="1.8"/></svg></span>The leap into electronic typesetting, remaining</li>
    <li><span class="tick"><svg width="10" height="10" viewBox="0 0 10 10"><path d="M1.5 5.2l2.4 2.4 4.6-5" fill="none" stroke="#8cc63f" stroke-width="1.8"/></svg></span>It was popularised in the 1960s</li>
  </ul>
  <div class="coins abs" role="img" aria-label="Stacks of gold coins"></div>
  <svg class="arrow abs" style="left:8px;top:92px" width="14" height="22" viewBox="0 0 14 22"><path d="M11 2L3 11l8 9" fill="none" stroke="#fff" stroke-width="3"/></svg>
  <svg class="arrow abs" style="left:714px;top:86px" width="14" height="22" viewBox="0 0 14 22"><path d="M3 2l8 9-8 9" fill="none" stroke="#fff" stroke-width="3"/></svg>
</section>

<h2 class="discover-title abs display">Discover Amazing projects or<br>Start your own for Free</h2>
<p class="discover-text abs">Lorem Ipsum is simply dummy text of the printing and typesetting industry. Lorem Ipsum has been the industry's standard dummy text ever since the 1500s.</p>
<div class="start-btn abs">
  <svg width="15" height="15" viewBox="0 0 20 20"><path d="M10 1l2.7 6 6.3.6-4.8 4.2 1.4 6.4L10 15l-5.6 3.2 1.4-6.4L1 7.6 7.3 7z" fill="#fff"/></svg>
  START NOW
</div>

<section class="projects abs"></section>
<div class="tabs abs">
  <span><svg width="9" height="9" viewBox="0 0 10 10"><circle cx="5" cy="5" r="4" fill="none" stroke="#333" stroke-width="1.2"/><circle cx="5" cy="5" r="1.5" fill="#333"/></svg>Most Populor</span>
  <span><svg width="8" height="10" viewBox="0 0 8 10"><path d="M4 10C1 6 .5 5 .5 3.8a3.5 3.5 0 017 0C7.5 5 7 6 4 10z" fill="#333"/><circle cx="4" cy="3.8" r="1.3" fill="#fff"/></svg>Near Me</span>
  <span><svg width="10" height="9" viewBox="0 0 10 9"><path d="M1 3h7M6 1l2 2-2 2M9 6H2M4 4L2 6l2 2" fill="none" stroke="#333" stroke-width="1.2"/></svg>Live Feed</span>
  <span><svg width="8" height="10" viewBox="0 0 8 10"><circle cx="4" cy="2.7" r="2.2" fill="#333"/><path d="M0 10c0-3 1.8-4.5 4-4.5S8 7 8 10z" fill="#333"/></svg>Funded Buy Friends</span>
</div>

<ul class="categories abs">
  <li>Art</li><li>Comics</li><li>Dance</li><li>Design</li><li>Fashion</li><li>Film &amp; Video</li><li>Food</li><li>Games</li><li>Music</li><li>Photography</li><li>Publishing</li><li>Technology</li><li>Theater</li><li>Weddings</li>
</ul>
<div class="more-link abs">more categories</div>
<div class="view-all abs">View All</div>

<article class="card abs" style="left:216px;top:488px">
  <div class="card-media" role="img" aria-label="Photo of a music band posing" style="background:linear-gradient(#8a7a66,#4a3b2e)"><div class="price">$ 9450</div></div>
  <div class="card-body"><div class="card-name">Project Name</div><p class="card-text">It was popularised in the 1960s with the release of Letraset sheets.</p>
  <div class="progress"><i style="width:50%"></i></div>
  <div class="stats"><span>Funded<b>50%</b></span><span>owner<b>Tom Hale</b></span><span>Days left<b>20</b></span></div></div>
</article>
<article class="card abs" style="left:368px;top:488px">
  <div class="card-media" role="img" aria-label="Photo of an open vintage magazine" style="background:linear-gradient(#d9c9c4,#9a8a88)"><div class="price">$ 650</div></div>
  <div class="card-body"><div class="card-name">Project Name</div><p class="card-text">It was popularised in the 1960s with the release of Letraset sheets.</p>
  <div class="progress"><i style="width:20%"></i></div>
  <div class="stats"><span>Funded<b>50%</b></span><span>owner<b>Tom Hale</b></span><span>Days left<b>10</b></span></div></div>
</article>
<article class="card abs" style="left:522px;top:488px">
  <div class="card-media" role="img" aria-label="Photo of villagers in a sunny field" style="background:linear-gradient(#d8a54a,#6e5a2a)"><div class="price">$ 3930</div></div>
  <div class="card-body"><div class="card-name">Project Name</div><p class="card-text">It was popularised in the 1960s with the release of Letraset sheets.</p>
  <div class="progress late"><i style="width:75%"></i></div>
  <div class="stats"><span>Funded<b>50%</b></span><span>owner<b>Tom Hale</b></span><span>Days left<b>1</b></span></div></div>
</article>
<article class="card abs" style="left:216px;top:656px">
  <div class="card-media" role="img" aria-label="Portrait photo of a woman in a blue scarf" style="background:linear-gradient(#3d5f86,#1d2738)"><div class="price">$ 993</div></div>
  <div class="card-body"><div class="card-name">Project Name</div><p class="card-text">It was popularised in the 1960s with the release of Letraset sheets.</p>
  <div class="progress"><i style="width:20%"></i></div>
  <div class="stats"><span>Funded<b>50%</b></span><span>owner<b>Tom Hale</b></span><span>Days left<b>8</b></span></div></div>
</article>
<article class="card abs" style="left:368px;top:656px">
  <div class="card-media" role="img" aria-label="Photo of a crowd gathered around a screen" style="background:linear-gradient(#8e9396,#3b3f42)"><div class="price">$543</div></div>
  <div class="card-body"><div class="card-name">Project Name</div><p class="card-text">It was popularised in the 1960s with the release of Letraset sheets.</p>
  <div class="progress"><i style="width:50%"></i></div>
  <div class="stats"><span>Funded<b>50%</b></span><span>owner<b>Tom Hale</b></span><span>Days left<b>30</b></span></div></div>
</article>
<article class="card abs" style="left:522px;top:656px">
  <div class="card-media" role="img" aria-label="Hand-drawn sketch illustration" style="background:linear-gradient(#eef0f6,#b7bccd)"><div class="price">$ 2250</div></div>
  <div class="card-body"><div class="card-name">Project Name</div><p class="card-text">It was popularised in the 1960s with the release of Letraset sheets.</p>
  <div class="progress"><i style="width:50%"></i></div>
  <div class="stats"><span>Funded<b>50%</b></span><span>owner<b>Tom Hale</b></span><span>Days left<b>35</b></span></div></div>
</article>

<h2 class="stories-title abs display">Successfull stories</h2>
<p class="stories-text abs">Rem Ipsum has been the industry's standard dummy text ever since the 1500s, when an unknown printer took a galley of type and scrambled it to make a t</p>
<div class="avatar abs" style="left:94px;background:radial-gradient(#b9b6b2,#55504c)" role="img" aria-label="Portrait of a project owner"></div>
<div class="avatar abs" style="left:192px;background:radial-gradient(#c79a7a,#5e4635)" role="img" aria-label="Portrait of a project owner"></div>
<div class="avatar abs" style="left:291px;background:radial-gradient(#a98d72,#3d3a2c)" role="img" aria-label="Portrait of a project owner"></div>
<div class="avatar abs" style="left:390px;background:radial-gradient(#b98a70,#3e2a22)" role="img" aria-label="Portrait of a project owner"></div>
<div class="avatar abs" style="left:489px;background:radial-gradient(#d7b39b,#6d7f5a)" role="img" aria-label="Portrait of a project owner"></div>
<div class="avatar abs" style="left:589px;background:radial-gradient(#a06c52,#8a5fa8)" role="img" aria-label="Portrait of a project owner"></div>

<footer class="site-footer abs"></footer>
<h3 class="foot-h abs display" style="left:79px">About us</h3>
<p class="foot-p abs" style="left:79px;top:1067px;width:170px">Rem Ipsum has been the industry's standard dummy text ever since the 1500s, when an unknown printer took a galley of type and scrambled it to make a t</p>
<p class="foot-p abs" style="left:79px;top:1118px;color:var(--green-dark)">info@lumopledge-hub.com</p>
<p class="foot-p abs" style="left:79px;top:1131px;color:var(--green-dark)">call: 00 000 00</p>

<h3 class="foot-h abs display" style="left:279px">Quick Links</h3>
<ul class="foot-links abs" style="left:279px;top:1067px"><li>Link name</li><li>Link name</li><li>Link name</li><li>Link name</li><li>Link name</li></ul>
<ul class="foot-links abs" style="left:360px;top:1064px"><li>Link name</li><li>Link name</li><li>Link name</li><li>Link name</li><li>Link name</li></ul>

<h3 class="foot-h abs display" style="left:462px;top:1038px">News Letter</h3>
<p class="foot-p abs" style="left:462px;top:1066px;width:200px">Rem Ipsum has been the industry's standard dummy text ever since the 1500s, when an unknown printer took a galley of type and scrambled it to make a t</p>
<div class="newsletter abs">Enter your email address<span class="subscribe">SUBSCRIBE</span></div>

<div class="bottom-bar abs">Copyright © 2013 lumopledge. All rights reserved</div>

</body>
</html>
```